Divorce Lawyer print and ebook cover (Planting gardens after every storm )

I need a front and back cover for my divorce and family law book. I already have a photo and title. The back cover photo is not necessary but can be interesting the Front-main cover is a must

Target Market(s)

Prospective client

Colors

Designer to choose colors to be used in the design.

Requirements
Must have
• Front photo by viewable.

```html
<!DOCTYPE html>
<html lang="en">
<head>
<meta charset="utf-8">
<title>Planting Gardens After Every Storm – Cover</title>
<link rel="stylesheet" href="https://fonts.googleapis.com/css2?family=Marcellus&family=Abril+Fatface&family=Arimo&display=swap">
<style>
  :root {
    --page-bg: #e9ecef;
    --paper: #e4e4e3;
    --paper-light: #eeeeed;
    --ink: #0b0c0d;
    --fog-blue: #8fa3b3;
    --fog-light: #dfe7ec;
    --canopy-gold: #d8b85a;
    --canopy-green: #a9bf5e;
    --road-dark: #23272b;
    --road-mid: #3b3f41;
  }
  * { margin: 0; padding: 0; box-sizing: border-box; }
  html, body {
    width: 1200px;
    height: 1200px;
    overflow: hidden;
    background: var(--page-bg);
  }
  .canvas {
    width: 1200px;
    height: 1200px;
    display: flex;
    align-items: center;
    justify-content: center;
  }
  .cover {
    width: 730px;
    height: 1100px;
    display: flex;
    flex-direction: column;
    background: var(--paper);
  }
  .cover-photo {
    height: 584px;
    position: relative;
    background:
      linear-gradient(180deg, rgba(0,0,0,0) 0%, rgba(0,0,0,0) 52%, var(--road-mid) 75%, var(--road-dark) 100%),
      radial-gradient(ellipse at 35% 10%, var(--fog-light) 0%, rgba(223,231,236,0) 45%),
      linear-gradient(90deg, #4f6272 0%, var(--fog-blue) 35%, #c9cbb4 55%, var(--canopy-gold) 78%, var(--canopy-green) 100%);
  }
  .cover-text {
    flex: 1;
    display: flex;
    flex-direction: column;
    align-items: center;
    background: radial-gradient(ellipse at 50% 40%, var(--paper-light) 0%, var(--paper) 80%);
    color: var(--ink);
    text-align: center;
  }
  .title-top {
    margin-top: 60px;
    font-family: "Marcellus", serif;
    font-size: 54px;
    letter-spacing: 1px;
    line-height: 1;
  }
  .title-middle {
    margin-top: 34px;
    display: flex;
    align-items: center;
    gap: 20px;
    font-family: "Marcellus", serif;
    font-size: 34px;
    line-height: 1;
  }
  .title-rule { width: 110px; height: 8px; }
  .title-main {
    margin-top: 26px;
    font-family: "Abril Fatface", serif;
    font-size: 118px;
    line-height: 1;
  }
  .author {
    margin-top: 64px;
    font-family: "Arimo", sans-serif;
    font-size: 32px;
    line-height: 1;
  }
</style>
</head>
<body>
  <main class="canvas">
    <article class="cover">
      <div class="cover-photo" role="img" aria-label="Photo of a man in a dark suit standing at a fork in a misty forest road, with a signpost pointing left to a grey foggy path and right to a sunlit green path"></div>
      <div class="cover-text">
        <h1 class="title-top">PLANTING GARDENS</h1>
        <div class="title-middle">
          <svg class="title-rule" viewBox="0 0 110 8" aria-hidden="true"><polygon points="0,4 110,0 110,8" fill="var(--ink)"/></svg>
          <span>AFTER EVERY</span>
          <svg class="title-rule" viewBox="0 0 110 8" aria-hidden="true"><polygon points="0,0 110,4 0,8" fill="var(--ink)"/></svg>
        </div>
        <p class="title-main">Storm</p>
        <p class="author">Author Name</p>
      </div>
    </article>
  </main>
</body>
</html>
```